Stationery Design Project for a consulting/educational company

We need a stationery design for a consulting / educational company called "VORT d.o.o.". We are an official partner (yet stand-alone company) of the MELQ Institute, Germany (www.melq-example.de) that covers practically all themes regarding production optimisation, efectiveness, productivity (time studies, workplace organisation,...) We need the design for:

- a CERTIFICATE for seminar participates
- business cards
- letterhead

We are changing our webpage to their design, so we need to change the stationaries as well. I included 2 current logos, one with current color scheme (not important) and the other black/white with a frame. I also included the MELQ original certificate. Only the font + name"VORT" is important, the rest is up to you
Updates

Designs look good, but perhaps a gray & green combo would look nicer? Like on www.melq-example.de? And without the frames?

Target Market(s)

Larger production companies top and middle management

Industry/Entity Type

Business

Requirements
Must have
• - the stationaries (all of them) should, besides the company name "VORT", also include the logo MELQ (in its color), like on their webpage www.melq-example.de
Nice to have
• - certificate could use 5th color (e.g. silver) to make an impression
- similar color scheme to www.melq-example.de

```html
<!DOCTYPE html>
<html lang="en">
<head>
<meta charset="utf-8">
<title>VORT d.o.o. – Seminar Certificate</title>
<link rel="stylesheet" href="https://fonts.googleapis.com/css2?family=Arimo:wght@400;700&family=UnifrakturMaguntia&display=swap">
<style>
  :root {
    --teal: #14adb2;
    --ink: #1a1a1a;
    --rule: #d4d6d8;
    --silver-light: #c9d3d8;
    --silver-dark: #8e9aa2;
    --paper: #ffffff;
    --signature-tone-a: #efeae4;
    --signature-tone-b: #e3ddd6;
  }
  * { margin: 0; padding: 0; box-sizing: border-box; }
  html, body { width: 1200px; height: 912px; overflow: hidden; background: var(--paper); }
  .certificate {
    position: relative;
    width: 1200px;
    height: 912px;
    background: var(--paper);
    font-family: "Arimo", Arial, sans-serif;
    color: var(--ink);
  }
  .company-name {
    position: absolute;
    left: 62px;
    top: 82px;
    font-family: "Arimo", Arial, sans-serif;
    font-weight: 700;
    font-size: 78px;
    letter-spacing: 4px;
    line-height: 1;
    color: var(--teal);
  }
  .partner-band {
    position: absolute;
    left: 1101px;
    top: 0;
    width: 26px;
    height: 206px;
    background: var(--teal);
  }
  .partner-name {
    position: absolute;
    left: 1053px;
    top: 205px;
    transform-origin: 0 0;
    transform: rotate(-90deg);
    width: 162px;
    text-align: center;
    font-family: "Arimo", Arial, sans-serif;
    font-weight: 700;
    font-size: 42px;
    letter-spacing: 3px;
    line-height: 44px;
    color: var(--ink);
  }
  .title {
    position: absolute;
    left: 0;
    top: 196px;
    width: 1200px;
    text-align: center;
    font-family: "UnifrakturMaguntia", "Times New Roman", serif;
    font-size: 124px;
    line-height: 1.1;
    background: linear-gradient(100deg, var(--silver-dark) 0%, var(--silver-light) 35%, var(--silver-dark) 55%, var(--silver-light) 80%, var(--silver-dark) 100%);
    -webkit-background-clip: text;
    background-clip: text;
    color: transparent;
  }
  .presented-to {
    position: absolute;
    left: 0;
    top: 381px;
    width: 1200px;
    text-align: center;
    font-size: 26px;
    letter-spacing: 6px;
    color: var(--ink);
  }
  .name-rule {
    position: absolute;
    left: 210px;
    width: 792px;
    height: 1px;
    background: var(--rule);
  }
  .name-rule.upper { top: 460px; }
  .name-rule.lower { top: 574px; }
  .corner-frames { position: absolute; left: 0; top: 0; }
  .signature {
    position: absolute;
    border-radius: 6px;
    background: linear-gradient(90deg, var(--signature-tone-a), var(--signature-tone-b));
  }
  .signature.director { left: 180px; top: 686px; width: 155px; height: 56px; }
  .signature.partner { left: 480px; top: 692px; width: 112px; height: 54px; }
  .seal {
    position: absolute;
    left: 596px;
    top: 660px;
    width: 146px;
    height: 146px;
    border-radius: 50%;
    border: 1.5px solid var(--teal);
  }
  .signoff-rule {
    position: absolute;
    top: 754px;
    width: 157px;
    height: 1px;
    background: var(--rule);
  }
  .signoff-rule.director { left: 177px; }
  .signoff-rule.date { left: 845px; }
  .signoff-label {
    position: absolute;
    top: 768px;
    width: 200px;
    text-align: center;
    font-size: 16px;
    color: var(--ink);
  }
  .signoff-label.director { left: 155px; }
  .signoff-label.date { left: 822px; }
</style>
</head>
<body>
<main class="certificate">
  <div class="company-name">VORT</div>
  <div class="partner-band"></div>
  <div class="partner-name">MELQ</div>

  <h1 class="title">Certificate</h1>
  <p class="presented-to">Presented to</p>
  <div class="name-rule upper"></div>
  <div class="name-rule lower"></div>

  <svg class="corner-frames" width="1200" height="912" viewBox="0 0 1200 912" aria-hidden="true">
    <g fill="none" stroke="var(--teal)" stroke-width="3.5">
      <polyline points="66,648 66,858 307,858"/>
      <polyline points="86,665 86,840 290,840"/>
      <polyline points="1134,648 1134,858 893,858"/>
      <polyline points="1115,665 1115,840 912,840"/>
    </g>
  </svg>

  <div class="signature director" role="img" aria-label="Handwritten signature of the managing director"></div>
  <div class="signoff-rule director"></div>
  <div class="signoff-label director">Managing Director</div>

  <div class="signature partner" role="img" aria-label="Handwritten signature of the partner institute representative"></div>
  <div class="seal" role="img" aria-label="Partner institute seal"></div>

  <div class="signoff-rule date"></div>
  <div class="signoff-label date">Dated</div>
</main>
</body>
</html>
```